Occupational Therapy Clinic Advertisement

Create an advertisement for a magazine. Below I have attached my original ad (Ad 2020.pdf) . I want the ad changed and it should be eye catching. I would like a eye catching graphics added in the ad. It should be a graphic image that applies to education. I am attaching a sample graphic image of that I liked from someone elses ad- it should not be the same- it just is there to show what I like. Please use the same words from my original ad.Dimensions: 3.75in x 10.3 in

Target Market(s)

Parents of School aged children

Requirements
Must have
• Must have eye catching Graphic. Colors should be eye catching for a typed magazine.

```html
<!DOCTYPE html>
<html lang="en">
<head>
<meta charset="utf-8">
<title>Bright Path OT Services</title>
<link rel="stylesheet" href="https://fonts.googleapis.com/css2?family=Sniglet:wght@400&family=Bitter:ital,wght@1,500&family=Open+Sans:wght@400;600;700&display=swap">
<style>
  :root {
    --sky-top: #7ff3e2;
    --sky-mid: #8ef0f7;
    --sky-low: #a3f6fb;
    --wave-light: #b6fbf3;
    --grass: #b5ee3e;
    --grass-light: #d9f67a;
    --magenta: #f02fd6;
    --pink-wave: #f53ac8;
    --ink: #111111;
    --white: #ffffff;
    --strike: #e0262b;
    --badge-edge: #3fb8f0;
  }
  * { box-sizing: border-box; margin: 0; padding: 0; }
  html, body { width: 1200px; height: 3293px; overflow: hidden; background: #fff; }
  .ad {
    position: relative;
    width: 1200px;
    height: 3293px;
    overflow: hidden;
    background: linear-gradient(180deg, var(--sky-top) 0%, var(--sky-mid) 30%, var(--sky-low) 55%, var(--sky-low) 100%);
    color: var(--ink);
    font-family: "Open Sans", sans-serif;
  }
  .backdrop { position: absolute; inset: 0; width: 1200px; height: 3293px; }
  .block { position: absolute; left: 0; width: 1200px; text-align: center; white-space: nowrap; }
  .outlined {
    font-family: "Sniglet", cursive;
    font-weight: 400;
    color: var(--white);
    -webkit-text-stroke: 6px var(--ink);
    paint-order: stroke fill;
    line-height: 1;
  }
  .brand-name { top: 110px; font-size: 150px; }
  .brand-service { top: 305px; font-size: 108px; }
  .brand-phone { top: 435px; font-size: 104px; letter-spacing: -3px; }

  .concerns { position: absolute; left: 180px; top: 628px; list-style: none; }
  .concerns li {
    position: relative;
    padding-left: 55px;
    margin-bottom: 40px;
    font-family: "Bitter", serif;
    font-style: italic;
    font-weight: 500;
    font-size: 56px;
    line-height: 64px;
    letter-spacing: 1px;
    white-space: nowrap;
  }
  .concerns li::before {
    content: "";
    position: absolute;
    left: 0; top: 24px;
    border-left: 24px solid var(--ink);
    border-top: 11px solid transparent;
    border-bottom: 11px solid transparent;
  }
  .concerns li::after {
    content: "";
    position: absolute;
    left: 4px; top: 30px;
    border-left: 12px solid var(--sky-mid);
    border-top: 5px solid transparent;
    border-bottom: 5px solid transparent;
  }

  .promise {
    top: 1140px;
    font-family: "Sniglet", cursive;
    font-weight: 400;
    font-size: 70px;
    line-height: 114px;
    letter-spacing: -1px;
  }
  .promise .struck { position: relative; display: inline-block; }
  .promise .struck::after {
    content: "";
    position: absolute;
    left: -4px; right: -4px; top: 54%;
    height: 4px;
    background: var(--strike);
    transform: rotate(-14deg);
  }
  .heading-pink {
    font-family: "Sniglet", cursive;
    font-weight: 400;
    color: var(--magenta);
    font-size: 66px;
    line-height: 1;
  }
  .evaluate-head { top: 1372px; }
  .evaluate-text { top: 1462px; font-size: 52px; line-height: 70px; }
  .treat-head { top: 1548px; }
  .treat-list { position: absolute; left: 100px; top: 1630px; list-style: none; font-size: 52px; line-height: 76px; letter-spacing: 0.5px; white-space: nowrap; }
  .treat-list li::before { content: "\2605"; font-size: 38px; margin-right: 20px; vertical-align: 6px; }

  .artwork {
    position: absolute;
    left: 40px; top: 1860px;
    width: 1120px; height: 820px;
    border-radius: 60px 60px 200px 200px;
    background: radial-gradient(ellipse at 50% 45%, #f9e7b9 0%, #aef5f4 38%, #b9f15a 78%, rgba(181,238,62,0) 100%);
  }
  .age-badge { position: absolute; left: 495px; top: 1795px; width: 240px; height: 240px; }
  .age-badge p {
    position: absolute; inset: 0;
    display: flex; flex-direction: column; justify-content: center; align-items: center;
    font-weight: 700; font-size: 54px; line-height: 58px;
  }

  .accepted { top: 2718px; font-weight: 700; font-size: 50px; letter-spacing: 0.5px; }
  .location { top: 2808px; font-weight: 700; font-size: 42px; }
  .location svg { width: 34px; height: 44px; vertical-align: -6px; margin-right: 16px; }
  .eval-sites { top: 2862px; font-size: 42px; }
  .eval-sites strong, .email-line strong { font-weight: 700; }
  .info { top: 2946px; font-size: 42px; }
  .email-line { top: 3000px; font-size: 42px; }
  .email-line svg { width: 38px; height: 26px; vertical-align: -2px; margin-right: 10px; }
  .therapist { top: 3090px; left: 50px; font-weight: 700; font-size: 42px; line-height: 54px; }
</style>
</head>
<body>
<main class="ad">
  <svg class="backdrop" viewBox="0 0 1200 3293" aria-hidden="true">
    <path d="M0 0 H1200 V430 C1120 360 1060 250 1110 160 C1150 90 1000 40 880 90 C720 150 620 40 480 70 C330 100 240 40 120 110 C40 160 60 300 0 420 Z" fill="var(--wave-light)" opacity="0.6"/>
    <path d="M0 0 H1200 V180 C1080 120 980 30 820 60 C650 90 560 10 380 40 C230 60 120 10 0 60 Z" fill="var(--sky-top)" opacity="0.8"/>
    <path d="M0 1760 C90 1770 170 1840 210 1960 L220 3293 H0 Z" fill="var(--grass)"/>
    <path d="M1200 1760 C1110 1790 1030 1880 1010 1990 L1000 3293 H1200 Z" fill="var(--grass)"/>
    <path d="M0 2560 C300 2520 900 2520 1200 2560 V3293 H0 Z" fill="var(--grass-light)"/>
    <path d="M0 3010 C140 3040 230 3080 300 3140 C420 3240 800 3240 920 3120 C1000 3040 1100 3000 1200 2990 V3293 H0 Z" fill="var(--pink-wave)"/>
    <path d="M40 3293 C180 3180 360 3170 600 3190 C840 3210 1000 3160 1160 3293 Z" fill="var(--grass-light)"/>
  </svg>

  <h1 class="block outlined brand-name">Bright Path</h1>
  <p class="block outlined brand-service">OT Services</p>
  <p class="block outlined brand-phone">(555) 014-2288</p>

  <ul class="concerns">
    <li>Does your child struggle<br>with Reading/Kriah?</li>
    <li>Knows the information<br>but fails the test?</li>
    <li>Has difficulty remembering<br>names and dates?</li>
  </ul>

  <p class="block promise">Yes Your Child <span class="struck">can</span> Will Succeed<br>in School!</p>

  <h2 class="block heading-pink evaluate-head">We Evaluate:</h2>
  <p class="block evaluate-text">Using standardized Evaluations</p>
  <h2 class="block heading-pink treat-head">We Treat:</h2>
  <ul class="treat-list">
    <li>Using researched based techniques</li>
    <li>The underlying processing deficits</li>
  </ul>

  <div class="artwork" role="img" aria-label="Illustration of a child in a graduation cap sitting on an open book, with a pencil rocket, crayons, an apple, a school backpack and a clock"></div>

  <div class="age-badge">
    <svg viewBox="0 0 240 240" width="240" height="240" aria-hidden="true">
      <polygon fill="var(--white)" stroke="var(--badge-edge)" stroke-width="6" points="120,8 138,38 168,16 172,52 208,44 196,78 230,92 202,114 228,140 194,150 208,184 172,180 166,216 138,196 120,230 102,196 74,216 68,180 32,184 46,150 12,140 38,114 10,92 44,78 32,44 68,52 72,16 102,38"/>
    </svg>
    <p><span>Ages:</span><span>6-18</span></p>
  </div>

  <p class="block accepted">BOARD OF ED OT RSA'S ACCEPTED</p>
  <p class="block location">
    <svg viewBox="0 0 34 44" aria-hidden="true"><path d="M17 2 C8 2 2 9 2 17 C2 28 17 42 17 42 C17 42 32 28 32 17 C32 9 26 2 17 2 Z" fill="none" stroke="var(--magenta)" stroke-width="4"/><circle cx="17" cy="17" r="5" fill="var(--magenta)"/></svg>Located in Borough Park
  </p>
  <p class="block eval-sites">Evaluations done in <strong>Borough Park &amp; Staten Island</strong></p>
  <p class="block info">For more information or to be added to our email list,</p>
  <p class="block email-line">
    <svg viewBox="0 0 38 26" aria-hidden="true"><rect x="1" y="1" width="36" height="24" fill="none" stroke="var(--badge-edge)" stroke-width="2"/><path d="M1 1 L19 15 L37 1" fill="none" stroke="var(--badge-edge)" stroke-width="2"/></svg>please email: <strong>brightpathot@example.com</strong>
  </p>
  <p class="block therapist">Dana Feldman OTR/L<br>(555)014-2288</p>
</main>
</body>
</html>
```